A new healing and spiritual podcast needs a design.

We need a design for the podcast that will also be used on the supporting website. The name is Still Lantern Path. The podcast will be about tapping into our own guidance to have a great life. There will be interviews, meditations, discussions on all aspects of energy healing and alternative healing techniques. The website will be where classes will be offered. Looking for something that conveys a peaceful feeling without looking too "healy-feely". Yet also want it to get peoples attention.

Target Market(s)

Metaphysical, spiritual (not religious), energy healers

Font styles to use
Serif

Requirements
Must have
• The name "Still Lantern Path"
Nice to have
• I'd like it to be inviting, catch peoples eye, convey a peaceful feeling, yet not be boring.
Should not have
• Animated (like comic strip) images.

```html
<!DOCTYPE html>
<html lang="en">
<head>
<meta charset="utf-8">
<title>Still Lantern Path</title>
<link rel="stylesheet" href="https://fonts.googleapis.com/css2?family=Gloock&display=swap">
<style>
  :root {
    --bg-orange: #ec9152;
    --cream: #f1dcc4;
    --star-rust: #c4552b;
    --star-soft: #e07a3c;
    --photo-amber: #d98a4a;
    --photo-gold: #e9ad6a;
    --photo-rust: #a9552d;
    --photo-deep: #5e2f18;
    --glow: #fff1d6;
  }
  html, body {
    margin: 0;
    padding: 0;
    width: 1200px;
    height: 1200px;
    overflow: hidden;
    background: var(--bg-orange);
  }
  .cover {
    position: relative;
    width: 1200px;
    height: 1200px;
    background: var(--bg-orange);
    overflow: hidden;
  }
  .cover__photo {
    position: absolute;
    left: 0;
    top: 340px;
    width: 1200px;
    height: 860px;
    background:
      radial-gradient(ellipse 260px 220px at 900px 450px, rgba(255, 236, 200, 0.85), rgba(255, 236, 200, 0) 70%),
      radial-gradient(ellipse 420px 120px at 420px 380px, rgba(248, 200, 150, 0.7), rgba(248, 200, 150, 0) 70%),
      radial-gradient(ellipse 340px 300px at 1150px 200px, rgba(120, 55, 25, 0.6), rgba(120, 55, 25, 0) 70%),
      radial-gradient(ellipse 420px 380px at 80px 620px, rgba(94, 47, 24, 0.75), rgba(94, 47, 24, 0) 70%),
      radial-gradient(ellipse 500px 260px at 700px 780px, rgba(110, 52, 24, 0.6), rgba(110, 52, 24, 0) 70%),
      linear-gradient(180deg, var(--bg-orange) 0%, var(--photo-gold) 20%, var(--photo-amber) 45%, var(--photo-rust) 75%, var(--photo-deep) 100%);
  }
  .cover__emblem {
    position: absolute;
    left: 760px;
    top: 640px;
    width: 320px;
    height: 320px;
    border-radius: 50%;
    background: radial-gradient(circle, rgba(255, 241, 214, 0.95) 0%, rgba(255, 241, 214, 0.55) 18%, rgba(255, 241, 214, 0.15) 45%, rgba(255, 241, 214, 0) 70%);
  }
  .cover__light-leaks {
    position: absolute;
    left: 0;
    top: 850px;
    width: 420px;
    height: 350px;
  }
  .cover__title {
    position: absolute;
    left: 0;
    top: 140px;
    width: 1200px;
    margin: 0;
    text-align: center;
    font-family: "Gloock", serif;
    font-weight: 400;
    font-size: 136px;
    line-height: 1.37;
    color: var(--cream);
    text-transform: uppercase;
    letter-spacing: 0.01em;
  }
  .cover__title-line {
    display: block;
  }
  .cover__star {
    position: absolute;
  }
  .cover__star--large { left: 90px; top: 415px; width: 165px; height: 180px; fill: var(--star-rust); }
  .cover__star--top { left: 1010px; top: 78px; width: 102px; height: 115px; fill: var(--star-soft); }
  .cover__star--small { left: 1095px; top: 156px; width: 66px; height: 72px; fill: var(--star-rust); }
</style>
</head>
<body>
  <main class="cover">
    <svg width="0" height="0" style="position:absolute">
      <defs>
        <symbol id="sparkle" viewBox="-50 -50 100 100">
          <polygon points="0,-50 4.2,-10.2 19.8,-19.8 10.2,-4.2 50,0 10.2,4.2 19.8,19.8 4.2,10.2 0,50 -4.2,10.2 -19.8,19.8 -10.2,4.2 -50,0 -10.2,-4.2 -19.8,-19.8 -4.2,-10.2"/>
        </symbol>
      </defs>
    </svg>

    <div class="cover__photo" role="img" aria-label="Warm, sunlit photograph of a hand reaching through wildflowers and tall grass in a golden meadow"></div>
    <div class="cover__emblem" role="img" aria-label="Glowing white sunburst emblem with a central eye over the meadow"></div>

    <svg class="cover__light-leaks" viewBox="0 0 420 350" aria-hidden="true" fill="none" stroke-linecap="round">
      <path d="M10 40 C 60 150, 90 250, 130 350" stroke="rgba(255,120,80,0.55)" stroke-width="10"/>
      <path d="M24 40 C 74 150, 104 250, 144 350" stroke="rgba(120,220,160,0.35)" stroke-width="6"/>
      <path d="M110 10 C 150 110, 200 230, 270 350" stroke="rgba(255,190,140,0.6)" stroke-width="12"/>
      <path d="M200 70 C 240 160, 290 260, 350 350" stroke="rgba(255,110,80,0.5)" stroke-width="10"/>
      <path d="M214 70 C 254 160, 304 260, 364 350" stroke="rgba(140,220,200,0.35)" stroke-width="6"/>
    </svg>

    <h1 class="cover__title">
      <span class="cover__title-line">Still Lantern</span>
      <span class="cover__title-line">Path</span>
    </h1>

    <svg class="cover__star cover__star--large" aria-hidden="true"><use href="#sparkle"/></svg>
    <svg class="cover__star cover__star--top" aria-hidden="true"><use href="#sparkle"/></svg>
    <svg class="cover__star cover__star--small" aria-hidden="true"><use href="#sparkle"/></svg>
  </main>
</body>
</html>
```